Harbor Nightclub

Nightclub flyer., digital single sided, for KV and PX. I included samples of some previous flyers we've used. Sample Info:
HARBOR
FRIDAYS
FRI MAY 1 2020
DJ VORTAN (club floor)
DJ RUZO & DJ TAV (residents on the lounge floor)
4217 Marlow Avenue Sacramento
www.harborvenuehall.example for list/VIP inquiries

Target Market(s)

Upscale top 40 crowd but want some cool and artsy like the examples included.

Font styles to use
Sans Serif

Requirements
Must have
• Harbor Logo
Nice to have
• Would be nice if the flyer can be incorporated later with DJ photos (sometimes we will add dj photos to pixagram etc). Would like a big city type of feel.
Should not have
• Nothing too sexual.

```html
<!DOCTYPE html>
<html lang="en">
<head>
<meta charset="utf-8">
<title>Harbor Fridays Flyer</title>
<link href="https://fonts.googleapis.com/css2?family=Archivo+Black&family=Montserrat:wght@400;500;800&display=swap" rel="stylesheet">
<style>
  :root {
    --page: #ffffff;
    --night: #07060c;
    --ink: #ffffff;
    --magenta: #d9276f;
    --glitch-red: #e0204e;
    --glitch-blue: #3a3cff;
  }
  * { margin: 0; padding: 0; box-sizing: border-box; }
  html, body { width: 1200px; height: 1000px; overflow: hidden; background: var(--page); }
  .flyer {
    position: absolute; left: 258px; top: 62px; width: 709px; height: 886px;
    background: var(--night); overflow: hidden;
    font-family: "Montserrat", sans-serif; color: var(--ink);
  }
  .flyer__backdrop { position: absolute; inset: 0; width: 100%; height: 100%; }
  .spaced { position: absolute; left: 0; width: 100%; text-align: center; text-transform: uppercase; font-weight: 400; }
  .flyer__address { top: 28px; font-size: 13px; letter-spacing: 6.4px; }
  .flyer__date { top: 120px; font-size: 22px; letter-spacing: 6px; font-weight: 500; }
  .flyer__title {
    position: absolute; left: 0; width: 100%; top: 172px; text-align: center;
    font-family: "Archivo Black", sans-serif; font-size: 128px; line-height: 1; letter-spacing: 2px;
    color: var(--night); -webkit-text-stroke: 2px var(--ink);
    text-shadow: -4px -3px 0 var(--glitch-blue), 4px 3px 0 var(--glitch-red);
    transform: perspective(500px) rotateX(18deg) skewX(-8deg) scaleX(1.05);
  }
  .lineup { position: absolute; left: 0; width: 100%; top: 460px; text-align: center; font-weight: 800; text-transform: uppercase; }
  .lineup__headliner { font-size: 42px; line-height: 40px; color: var(--magenta); }
  .lineup__residents { font-size: 38px; line-height: 40px; color: transparent; -webkit-text-stroke: 1.4px var(--ink); }
  .flyer__side-date {
    position: absolute; left: 2px; top: 622px; width: 230px; font-size: 12px; letter-spacing: 7px;
    text-transform: uppercase; transform: rotate(-90deg); transform-origin: left top; white-space: nowrap;
  }
  .brand { position: absolute; left: 0; width: 100%; top: 694px; display: flex; justify-content: center; align-items: center; gap: 8px; }
  .brand__dot { width: 32px; height: 32px; border-radius: 50%; background: var(--ink); }
  .brand__name { font-size: 20px; font-weight: 500; letter-spacing: 0.5px; }
  .flyer__web { top: 836px; font-size: 13px; letter-spacing: 5.5px; }
  .flyer__inquiries { top: 854px; font-size: 13px; letter-spacing: 5.5px; }
</style>
</head>
<body>
<main class="flyer">
  <svg class="flyer__backdrop" viewBox="0 0 709 886" preserveAspectRatio="none" role="img" aria-label="Deep space backdrop with violet nebula clouds and a glowing planet horizon lit with magenta city lights">
    <defs>
      <radialGradient id="nebula-top" cx="0.35" cy="0.08" r="0.7">
        <stop offset="0" stop-color="#3b2a7a"/>
        <stop offset="0.5" stop-color="#1e1545" stop-opacity="0.8"/>
        <stop offset="1" stop-color="#07060c" stop-opacity="0"/>
      </radialGradient>
      <radialGradient id="nebula-side" cx="0.05" cy="0.6" r="0.4">
        <stop offset="0" stop-color="#2a1d66" stop-opacity="0.8"/>
        <stop offset="1" stop-color="#07060c" stop-opacity="0"/>
      </radialGradient>
      <radialGradient id="planet-glow" cx="0.5" cy="0" r="0.6">
        <stop offset="0" stop-color="#5a1e6e"/>
        <stop offset="0.5" stop-color="#3a1450"/>
        <stop offset="1" stop-color="#120a24"/>
      </radialGradient>
      <linearGradient id="horizon" x1="0" y1="0" x2="0" y2="1">
        <stop offset="0" stop-color="#07060c" stop-opacity="0"/>
        <stop offset="1" stop-color="#6a1f5e" stop-opacity="0.7"/>
      </linearGradient>
    </defs>
    <rect width="709" height="886" fill="#07060c"/>
    <rect width="709" height="886" fill="url(#nebula-top)"/>
    <rect width="709" height="886" fill="url(#nebula-side)"/>
    <rect y="600" width="709" height="140" fill="url(#horizon)"/>
    <ellipse cx="354" cy="1250" rx="640" ry="530" fill="url(#planet-glow)"/>
  </svg>

  <p class="spaced flyer__address">4217 Marlow Avenue Sacramento</p>
  <p class="spaced flyer__date">Fri May 1 2020</p>
  <h1 class="flyer__title">FRIDAYS</h1>

  <div class="lineup">
    <p class="lineup__headliner">DJ Vortan</p>
    <p class="lineup__residents">DJ Ruzo &amp; DJ Tav</p>
  </div>

  <p class="flyer__side-date">Fri May 1 2020</p>

  <div class="brand">
    <span class="brand__dot"></span>
    <span class="brand__name">HARBOR</span>
  </div>

  <p class="spaced flyer__web">www.harborvenuehall.example</p>
  <p class="spaced flyer__inquiries">For List/VIP Inquiries</p>
</main>
</body>
</html>
```